Graphic background for 10 Pull Up Banners

To produce a graphic background for a 100 cm wide by 200 cm high Pull-Up Display banner containing a Buddhist text in three languages: Tibetan, Mandarin and English. Please refer to uploaded file "Elements of Pull Up Banner". The design should be simple (not drawing attention away from the text). This design should then be varied for or extended to the next banner and so on until the 10th banner. When the banners are lined up, they should form a single design that is 1000 cm wide by 200 cm high.
An alternative way to look at the project is to produce a graphic background of 1000 cm width by 200 cm height that is then splitted into ten separate 100 cm wide by 200 cm high graphic to be used as background for 10 Buddhist texts (text 1, 2, 3, 4, 5, 6, 7, 8, 9a, 9b) on 10 Pull-Up Display Banners, the text in each banner being in the three languages mentioned earlier.
In either perspective, the design should be simple and not draw attention away from the texts. See uploaded PDF file "Examples.pdf"
For attendees at a Buddhist Event.

```html
<!DOCTYPE html>
<html lang="en">
<head>
<meta charset="utf-8">
<title>Pull-Up Banner Series – Buddhist Texts</title>
<link rel="stylesheet" href="https://fonts.googleapis.com/css2?family=Noto+Serif+Tibetan:wght@400&family=Noto+Serif+SC:wght@400;600&family=Noto+Sans+SC:wght@400&family=Arimo:wght@400;700&display=swap">
<style>
:root{
  --page:#ffffff;
  --gold-top:#f3d04a;
  --gold-mid:#ecb93c;
  --gold-low:#e2a233;
  --band:#d99a22;
  --band-stripe:#f1c87f;
  --ink-title:#1b86c8;
  --ink-light:#fff7e0;
  --divider:rgba(255,240,200,.55);
  --emblem:#f8e2ad;
}
*{margin:0;padding:0;box-sizing:border-box}
html,body{width:1200px;height:1200px;overflow:hidden;background:var(--page)}
.canvas{position:relative;width:1200px;height:1200px;overflow:hidden}
.strip{position:absolute;height:346px;overflow:hidden;
  background:linear-gradient(180deg,var(--gold-top) 0%,var(--gold-mid) 45%,var(--gold-low) 84%)}
.strip-1{left:29px;top:66px;width:1171px}
.strip-2{left:0;top:436px;width:1200px}
.strip-3{left:0;top:798px;width:1156px}
.panel{position:absolute;top:0;width:173px;height:346px;border-right:1px dashed var(--divider);color:var(--ink-light)}
.panel-body{position:absolute;left:13px;right:8px;top:10px}
.stripe{position:absolute;left:0;right:0;top:289px;height:9px;background:var(--band-stripe)}
.band{position:absolute;left:0;right:0;top:298px;height:48px;background:var(--band)}
.emblem{position:absolute;left:50%;top:10px;width:28px;height:28px;margin-left:-14px;border-radius:50%;background:var(--emblem);opacity:.85}
.title-zh{font-family:"Noto Sans SC",sans-serif;font-size:6.5px;color:var(--ink-title);line-height:1.2}
.title-en{font-family:"Arimo",sans-serif;font-weight:700;font-size:6.2px;color:var(--ink-title);line-height:1.3}
.bo{font-family:"Noto Serif Tibetan",serif;font-size:8px;line-height:1.55;margin:6px 0 0 22px;white-space:nowrap}
.bo-small{font-family:"Noto Serif Tibetan",serif;font-size:4.2px;line-height:1.7;margin:6px 0 0 10px;white-space:nowrap}
.zh{font-family:"Noto Serif SC",serif;font-size:7.5px;line-height:2.55;margin:14px 0 0 32px;white-space:nowrap}
.zh-small{font-family:"Noto Serif SC",serif;font-size:4.3px;line-height:1.75;margin:10px 0 0 40px;white-space:nowrap}
.en{font-family:"Arimo",sans-serif;font-size:5.6px;line-height:1.35;margin-top:14px}
.en p+p{margin-top:5px}
.en-small{font-family:"Arimo",sans-serif;font-size:3.6px;line-height:1.4;margin-top:12px}
.en-small p+p{margin-top:3px}
.note{font-family:"Noto Serif SC",serif;font-size:4px;font-style:italic;margin:8px 0 0 30px;opacity:.85}
.two-col{display:flex;gap:8px;margin-top:6px}
.two-col .bo-small{margin:0}
.two-col .zh-small{margin:0}
.dedication{font-family:"Arimo",sans-serif;font-size:4.5px;color:var(--ink-title);margin-top:8px;letter-spacing:.3px}
</style>
</head>
<body>
<div class="canvas">

<!-- Row 1 -->
<section class="strip strip-1">
  <article class="panel" style="left:0">
    <div class="panel-body">
      <div class="title-zh">十个误解</div><div class="title-en">Ten Mistaking</div>
      <div class="bo-small">འདོད་པ་དད་པར་འཁྲུལ་བ།<br>ཆགས་པ་བརྩེ་བར་འཁྲུལ་བ།<br>བླང་དོར་མེད་པ་སྟོང་ཉིད་དུ་འཁྲུལ་བ།<br>ལྟ་བ་རྟོགས་པར་འཁྲུལ་བ།<br>སྒོམ་པ་ཉམས་སུ་འཁྲུལ་བ།<br>ཆོས་ལོག་ཆོས་སུ་འཁྲུལ་བ།<br>བདག་ཕན་གཞན་ཕན་དུ་འཁྲུལ་བ།</div>
      <div class="zh-small">贪心可能被误为信心，<br>执着可能被误为慈悲，<br>无念可能被误为空性，<br>见地可能被误为证悟，<br>禅修可能被误为觉受，<br>邪法可能被误为正法，<br>自利可能被误为利他。</div>
      <div class="en-small" style="margin-top:30px"><p>Desire can be mistaken for faith or devotion. Attachment can be mistaken for love and compassion. Conceptual emptiness can be mistaken for the emptiness of the nature of phenomena. Nihilism can be mistaken for the dharmadhatu. A meditative experience can be mistaken for realization. Outer religious practice can be mistaken for inner development of good qualities. An act to benefit yourself can be mistaken for an act to benefit others.</p></div>
    </div>
    <div class="stripe"></div><div class="band"><span class="emblem" role="img" aria-label="Lotus emblem"></span></div>
  </article>
  <article class="panel" style="left:174px">
    <div class="panel-body">
      <div class="title-zh">欲与爱</div><div class="title-en">Desire &amp; Attachment</div>
      <div class="bo">འདོད་པ་མེད་ན་དོན་མི་འགྲུབ།<br>འདོད་པ་ཀུན་ཆགས་པ་མ་ཡིན།<br>འདོད་ཆགས་ཁྱད་པར་མ་ཤེས་པར།<br>འདོད་ཆགས་ལམ་དུ་ཁྱེར་བ་བཞད།</div>
      <div class="zh">若无意欲则不成自利，<br>然若意欲非为执着故，<br>不知意欲执着差别即，<br>贪执说所当取确荒唐。</div>
      <div class="en" style="margin-top:22px"><p>If you have no desire, your goal cannot be achieved.<br>Since not all desire is attachment, not knowing how to differentiate desire from attachment, to talk about bringing passion into the path is absurd.</p></div>
    </div>
    <div class="stripe"></div><div class="band"><span class="emblem" role="img" aria-label="Butter lamp emblem"></span></div>
  </article>
  <article class="panel" style="left:347px">
    <div class="panel-body">
      <div class="title-zh">曾修过佛法的相状</div><div class="title-en">Signs Of Having Practised The Dharma</div>
      <div class="bo-small" style="font-size:5px">དལ་འབྱོར་གྱི་ལུས་ལ་སྙིང་པོ་ལེན་ན།<br>ཆོས་ཀྱི་སྙིང་པོ་རྙེད་པའི་རྟགས།<br>གསེར་དང་འོང་བ་མཉམ་པར་མཐོང་ན།<br>མི་རྟག་སྒྱུ་མ་སྐྱེས་པའི་རྟགས།<br>འཁོར་བའི་སྣང་བ་དགྲ་རུ་ཤར་ན།<br>ཕ་རོལ་ཏུ་ཕྱིན་པའི་རྟགས།</div>
      <div class="zh" style="font-size:6.3px;line-height:2.2;margin-left:26px">若懂舍自身富而修行，<br>表示取得真责精满「义」；<br><br>若懂金与土块平等观，<br>表示「无常」「如幻」心中生；<br><br>若视轮回现象为敌人，<br>表示渡往苦海之彼岸。</div>
      <div class="note">1. 暇满：八有暇和十圆满</div>
      <div class="en-small" style="margin-top:22px"><p>If you know not to cherish your body but use it to attain accomplishments in the Dharma, it is a sign that you have gotten the essence of your precious freedoms and fortunes.</p><p>If you know the sameness of gold and dirt while in meditative equipoise, it is a sign that the insight of impermanence and illusion have arisen in your mental continuum.</p><p>If you know to see samsaric phenomena as an enemy, it is a sign that you are heading to the other shore of the ocean of suffering.</p></div>
    </div>
    <div class="stripe"></div><div class="band"><span class="emblem" role="img" aria-label="Auspicious sign emblem"></span></div>
  </article>
  <article class="panel" style="left:521px">
    <div class="panel-body">
      <div class="title-zh">上师之恩德</div><div class="title-en">Kindness Of The Guru</div>
      <div class="bo">བླ་མ་དྲིན་ཅན་མ་བརྗེད་ཅིག<br>སངས་རྒྱས་མང་པོ་བྱོན་ན་ཡང་།<br>ངེད་ལ་སུ་ཡིས་མ་བཟུང་བ།<br>ཁྱེད་ཀྱིས་བརྩེ་བས་སྐྱོང་བར་མཛད།<br>སངས་རྒྱས་སྟོང་ལས་དྲིན་ཆེ་བ།</div>
      <div class="zh" style="margin-top:20px;line-height:1.9">切莫忘记上师，<br>即使众多佛降临，<br>谁皆未曾摄受我，<br>您不舍弃悲悯护，<br>您比千佛恩更大。</div>
      <div class="en-small" style="margin-top:34px"><p>Do not forget the guru.</p><p>Although many Buddhas had appeared, none has taken hold of me.</p><p>You did not abandon me, but lovingly and compassionately protected me.</p><p>Your kindness is greater than a thousand Buddhas'.</p></div>
    </div>
    <div class="stripe"></div><div class="band"><span class="emblem" role="img" aria-label="Endless knot emblem"></span></div>
  </article>
  <article class="panel" style="left:694px">
    <div class="panel-body">
      <div class="title-zh">您与佛法</div><div class="title-en">You And The Dharma</div>
      <div class="bo-small" style="font-size:4.6px">ཆོས་སྒོ་བརྒྱད་ཁྲི་བཞི་སྟོང་གི<br>རྩ་བ་རང་སེམས་འདུལ་བ་ཡིན།<br>རང་སེམས་མ་ཐུལ་ན་གདམས་པ་འབུམ།<br>ཐོས་ཀྱང་འཆི་དུས་ཕན་མི་ཐོགས།<br>ཆོས་སྐད་ཀྱིས་མི་ཕན་ཕྱི་མར་ཡང་།<br>ཆོས་ཀྱི་སྐད་ཆ་མང་མི་དགོས།<br>རང་སེམས་ཆོས་དང་འདྲེས་ན་གྲུབ།<br>གཞན་མི་དགའ་ཡང་ཆོས་ཀྱི་རྩེ།</div>
      <div class="zh-small" style="font-size:4.8px;margin-left:46px">八万四千法门之根本，<br>乃是调伏自心一者中，<br>未伏自烦恼闻十万教，<br>临终之时亦无所助益，<br>佛法术语于来世无益，<br>对于法言无须著名声，<br>唯自心与法相融合者，<br>纵他不喜亦为法之巅，<br>由实修而得成就故，<br>是为佛法之精要。</div>
      <div class="en-small" style="margin-top:14px"><p>The eighty-four thousand Dharma doors, are solely for subduing your own mind. If your mind is not tamed despite having received countless instructions, it is hard for these instructions to help you at the time of death. When the lofty Dharma language does not benefit you at the time of death, it is harder for them to benefit you in your next life. Thus, famous teachings are not needed. Instead, your mind and the Dharma should mix internally. And when through practice, you gained certainty, that is the peak of Dharma, even if others are not delighted about it.</p></div>
    </div>
    <div class="stripe"></div><div class="band"><span class="emblem" role="img" aria-label="Conch shell emblem"></span></div>
  </article>
  <article class="panel" style="left:868px">
    <div class="panel-body">
      <div class="title-zh">要避免的错误</div><div class="title-en">Mistakes To Avoid</div>
      <div class="bo">རྐང་པ་གར་འགྲོ་ལམ་མ་ནོར།<br>སྙིང་གཏད་ས་མི་མ་ནོར།<br>སྐྱབས་བཅོལ་ས་མགོན་མ་ནོར།<br>སེམས་ཁ་བཤད་ས་གྲོགས་མ་ནོར།</div>
      <div class="zh" style="margin-top:22px;line-height:2.5">足移动处路莫误。<br>心交托处人莫误。<br>所皈依处怙莫误。<br>说心声处友莫误。</div>
      <div class="en" style="margin-top:32px;font-size:5.3px"><p>Do not tread the wrong path.<br>Do not entrust your mind to the wrong person.<br>Do not seek refuge in the wrong guardian.<br>Do not confide your thoughts to the wrong friend.</p></div>
    </div>
    <div class="stripe"></div><div class="band"><span class="emblem" role="img" aria-label="Dharma wheel emblem"></span></div>
  </article>
  <article class="panel" style="left:1041px">
    <div class="panel-body">
      <div class="title-zh">别闲</div><div class="title-en">Don't Dally</div>
      <div class="bo">མ་ཡེངས་མ་ཡེངས་འཆི་བ་མྱུར།<br>འཆི་བ་གློ་བུར་བྱུང་ན་ཅི།<br>མ་ལེ་མ་ལེ་དམ་ཆོས་བརྩོན།<br>ཆོས་མེད་བར་དོར་སུ་ཡིས་སྐྱོབ།</div>
      <div class="zh" style="margin-top:18px;line-height:2.5;margin-left:26px">莫造莫造死亡迅速临。<br>死亡突然来到当何为？<br>莫停莫停精进于正法。<br>无法流转中有谁救护？</div>
      <div class="en" style="font-size:5.3px;margin-top:24px"><p>Don't be distracted, don't be distracted, for quickly death will come.</p><p>What can you do when death suddenly come?</p><p>Don't dally, don't dally, exert yourself in the excellent Dharma.</p><p>Without the Dharma, who can protect you when you wander in the bardo?</p></div>
    </div>
    <div class="stripe"></div><div class="band"><span class="emblem" role="img" aria-label="Golden fish emblem"></span></div>
  </article>
</section>

<!-- Row 2 -->
<section class="strip strip-2">
  <article class="panel" style="left:-119px">
    <div class="panel-body">
      <div class="title-zh">曾修过佛法的相状</div><div class="title-en">Signs Of Having Practised The Dharma</div>
      <div class="zh" style="font-size:6.3px;line-height:2.2;margin:70px 0 0 26px">若懂舍自身富而修行，<br>表示取得真责精满「义」；<br><br>若懂金与土块平等观，<br>表示「无常」「如幻」心中生；</div>
      <div class="en-small" style="margin-top:60px"><p>If you know not to cherish your body but use it to attain accomplishments in the Dharma, it is a sign that you have gotten the essence of your precious freedoms and fortunes.</p><p>If you know the sameness of gold and dirt while in meditative equipoise, it is a sign that the insight of impermanence and illusion have arisen in your mental continuum.</p></div>
    </div>
    <div class="stripe"></div><div class="band"><span class="emblem" role="img" aria-label="Auspicious sign emblem" style="left:auto;right:-4px"></span></div>
  </article>
  <article class="panel" style="left:54px">
    <div class="panel-body">
      <div class="title-zh">上师之恩德</div><div class="title-en">Kindness Of The Guru</div>
      <div class="bo">བླ་མ་དྲིན་ཅན་མ་བརྗེད་ཅིག<br>སངས་རྒྱས་མང་པོ་བྱོན་ན་ཡང་།<br>ངེད་ལ་སུ་ཡིས་མ་བཟུང་བ།<br>ཁྱེད་ཀྱིས་བརྩེ་བས་སྐྱོང་བར་མཛད།<br>སངས་རྒྱས་སྟོང་ལས་དྲིན་ཆེ་བ།</div>
      <div class="zh" style="margin-top:20px;line-height:1.9">切莫忘记上师，<br>即使众多佛降临，<br>谁皆未曾摄受我，<br>您不舍弃悲悯护，<br>您比千佛恩更大。</div>
      <div class="en-small" style="margin-top:34px"><p>Do not forget the guru.</p><p>Although many Buddhas had appeared, none has taken hold of me.</p><p>You did not abandon me, but lovingly and compassionately protected me.</p><p>Your kindness is greater than a thousand Buddhas'.</p></div>
    </div>
    <div class="stripe"></div><div class="band"><span class="emblem" role="img" aria-label="Endless knot emblem"></span></div>
  </article>
  <article class="panel" style="left:228px">
    <div class="panel-body">
      <div class="title-zh">您与佛法</div><div class="title-en">You And The Dharma</div>
      <div class="bo-small" style="font-size:4.6px">ཆོས་སྒོ་བརྒྱད་ཁྲི་བཞི་སྟོང་གི<br>རྩ་བ་རང་སེམས་འདུལ་བ་ཡིན།<br>རང་སེམས་མ་ཐུལ་ན་གདམས་པ་འབུམ།<br>ཐོས་ཀྱང་འཆི་དུས་ཕན་མི་ཐོགས།<br>ཆོས་སྐད་ཀྱིས་མི་ཕན་ཕྱི་མར་ཡང་།<br>ཆོས་ཀྱི་སྐད་ཆ་མང་མི་དགོས།<br>རང་སེམས་ཆོས་དང་འདྲེས་ན་གྲུབ།<br>གཞན་མི་དགའ་ཡང་ཆོས་ཀྱི་རྩེ།</div>
      <div class="zh-small" style="font-size:4.8px;margin-left:46px">八万四千法门之根本，<br>乃是调伏自心一者中，<br>未伏自烦恼闻十万教，<br>临终之时亦无所助益，<br>佛法术语于来世无益，<br>对于法言无须著名声，<br>唯自心与法相融合者，<br>纵他不喜亦为法之巅，<br>由实修而得成就故，<br>是为佛法之精要。</div>
      <div class="en-small" style="margin-top:14px"><p>The eighty-four thousand Dharma doors, are solely for subduing your own mind. If your mind is not tamed despite having received countless instructions, it is hard for these instructions to help you at the time of death. When the lofty Dharma language does not benefit you at the time of death, it is harder for them to benefit you in your next life. Thus, famous teachings are not needed. Instead, your mind and the Dharma should mix internally. And when through practice, you gained certainty, that is the peak of Dharma, even if others are not delighted about it.</p></div>
    </div>
    <div class="stripe"></div><div class="band"><span class="emblem" role="img" aria-label="Conch shell emblem"></span></div>
  </article>
  <article class="panel" style="left:402px">
    <div class="panel-body">
      <div class="title-zh">要避免的错误</div><div class="title-en">Mistakes To Avoid</div>
      <div class="bo">རྐང་པ་གར་འགྲོ་ལམ་མ་ནོར།<br>སྙིང་གཏད་ས་མི་མ་ནོར།<br>སྐྱབས་བཅོལ་ས་མགོན་མ་ནོར།<br>སེམས་ཁ་བཤད་ས་གྲོགས་མ་ནོར།</div>
      <div class="zh" style="margin-top:22px;line-height:2.5">足移动处路莫误。<br>心交托处人莫误。<br>所皈依处怙莫误。<br>说心声处友莫误。</div>
      <div class="en" style="margin-top:32px;font-size:5.3px"><p>Do not tread the wrong path.<br>Do not entrust your mind to the wrong person.<br>Do not seek refuge in the wrong guardian.<br>Do not confide your thoughts to the wrong friend.</p></div>
    </div>
    <div class="stripe"></div><div class="band"><span class="emblem" role="img" aria-label="Dharma wheel emblem"></span></div>
  </article>
  <article class="panel" style="left:575px">
    <div class="panel-body">
      <div class="title-zh">别闲</div><div class="title-en">Don't Dally</div>
      <div class="bo">མ་ཡེངས་མ་ཡེངས་འཆི་བ་མྱུར།<br>འཆི་བ་གློ་བུར་བྱུང་ན་ཅི།<br>མ་ལེ་མ་ལེ་དམ་ཆོས་བརྩོན།<br>ཆོས་མེད་བར་དོར་སུ་ཡིས་སྐྱོབ།</div>
      <div class="zh" style="margin-top:18px;line-height:2.5;margin-left:26px">莫造莫造死亡迅速临。<br>死亡突然来到当何为？<br>莫停莫停精进于正法。<br>无法流转中有谁救护？</div>
      <div class="en" style="font-size:5.3px;margin-top:24px"><p>Don't be distracted, don't be distracted, for quickly death will come.</p><p>What can you do when death suddenly come?</p><p>Don't dally, don't dally, exert yourself in the excellent Dharma.</p><p>Without the Dharma, who can protect you when you wander in the bardo?</p></div>
    </div>
    <div class="stripe"></div><div class="band"><span class="emblem" role="img" aria-label="Golden fish emblem"></span></div>
  </article>
  <article class="panel" style="left:749px">
    <div class="panel-body">
      <div class="title-zh">过于污垢</div><div class="title-en">Excessive Dirt</div>
      <div class="bo">ཕྲག་དོག་ཆེ་ན་སེམས་མི་སྐྱིད།<br>རང་དོན་ཆེ་ན་གྲོགས་མི་རྙེད།<br>སྙམ་པ་ཆེ་ན་དོན་མི་འགྲུབ།<br>གཡོ་སྒྱུ་ཆེ་ན་ཡིད་མི་ཆེས།</div>
      <div class="zh" style="margin-top:22px;line-height:2.5">嫉妒若盛心不乐。<br>自利若盛友不获。<br>贪妄若盛利不成。<br>狡诈若多人不信。</div>
      <div class="en" style="font-size:5.3px;margin-top:28px"><p>If your envy is great, your mind will not be joyful.</p><p>If your self-centredness is great, you will not gain friends.</p><p>If your greed is great, your goal will not be accomplished.</p><p>If your deceitfulness is great, your credibility will be lost</p></div>
    </div>
    <div class="stripe"></div><div class="band"><span class="emblem" role="img" aria-label="Turning arrows emblem"></span></div>
  </article>
  <article class="panel" style="left:922px">
    <div class="panel-body">
      <div class="title-zh">十大遗憾（上）</div><div class="title-en">Ten Regrets (Part I)</div>
      <div class="two-col">
        <div class="bo-small">མི་ལུས་རྙེད་དཀའ་ཐོབ་ཙམ་ན།<br>མི་དགེ་ལ་དགའ་བ་འགྱོད།<br>དལ་འབྱོར་ཐོབ་ཀྱང་ཆོས་མེད་པར།<br>ཕལ་པ་ཤི་བ་འགྱོད།<br>ཚེ་ཐུང་དོན་མེད་བྱ་བ་ལ།<br>ཚེ་ཟད་པ་ནི་འགྱོད།<br>སེམས་ཉིད་ཆོས་སྐུ་མ་རྟོགས་པར།<br>འཁོར་བར་བྱིང་བ་འགྱོད།<br>བླ་མ་ལས་བྲལ་འགྱོད།</div>
        <div class="zh-small">难得人身已获得，<br>行诸恶事甚可惜；<br>已具暇满无法修，<br>凡夫死去甚可惜；<br>寿短无益之事中，<br>耗尽此生甚可惜；<br>未悟心性法身者，<br>沉溺轮回甚可惜；<br>离别上师甚可惜。</div>
      </div>
      <div class="en-small" style="margin-top:48px"><p>It is regrettable to take joy in acts of non-virtues and evil when you have this unstained human body that is hard to obtain.</p><p>It is regrettable to die as an ordinary person without the Dharma, when you have this unstained human body with leisure, wealth and properties that is hard to obtain.</p><p>It is regrettable to exhaust yourself in senseless and meaningless activities in this age of degeneration when your human lifespan is short and will pass in an instant.</p><p>It is regrettable to be sunk in the mire of samsaric confusion when your unelaborated natural mind is the nature of dharmakaya.</p><p>It is regrettable to be separated from your holy guru, the guide on the path, before you attain enlightenment.</p></div>
    </div>
    <div class="stripe"></div><div class="band"><span class="emblem" role="img" aria-label="Treasure vase emblem"></span></div>
  </article>
  <article class="panel" style="left:1094px">
    <div class="panel-body">
      <div class="title-zh">十大遗憾（下）</div><div class="title-en">Ten Regrets (Part II)</div>
      <div class="two-col">
        <div class="bo-small">ཉམས་ལེན་མེད་པར་ཤི་བ་འགྱོད།<br>ཐོས་པ་ཆོས་སུ་མ་གྱུར་འགྱོད།<br>སྒོ་གསུམ་ཐ་མལ་བཞག་པ་འགྱོད།<br>དམ་ཚིག་ཉམས་པ་འགྱོད།<br>དགེ་བ་མ་བསགས་འགྱོད།</div>
        <div class="zh-small" style="margin:0">年少三门闲置者，<br>凡庸度日甚可惜；<br>闻法未成修持者，<br>空过此生甚可惜；<br>誓言毁坏甚可惜。</div>
      </div>
      <div class="en-small" style="margin-top:44px"><p>It is regrettable when the three doors of young adults in their prime, stay in the ordinary state of indifference (to practising the Dharma).</p><p style="font-style:italic;padding-left:8px">1. samskaras: those factors of the mind which cause (i) the aggregation into a being i.e. the taking of a rebirth; (ii) subsequent aggregation of the various forms of the five heaps of that rebirth; and (iii) the dissolution of that five heaps.</p><p style="font-style:italic;padding-left:8px">2. three doors: body, speech and mind</p></div>
      <div class="dedication">DEDICATION</div>
      <div class="bo-small" style="margin-left:8px">འགྲོ་བ་ཀུན་དང་མཉམ་དུ་སངས་རྒྱས་ཤོག</div>
      <div class="zh-small" style="margin:2px 0 0 8px">愿众有情共证佛果。</div>
      <div class="en-small" style="margin:2px 0 0 8px">May all attain Buddhahood together</div>
    </div>
    <div class="stripe"></div><div class="band"><span class="emblem" role="img" aria-label="Om syllable emblem"></span></div>
  </article>
</section>

<!-- Row 3 -->
<section class="strip strip-3">
  <article class="panel" style="left:-56px">
    <div class="panel-body">
      <div class="title-zh">上师之恩德</div><div class="title-en">Kindness Of The Guru</div>
      <div class="bo">བླ་མ་དྲིན་ཅན་མ་བརྗེད་ཅིག<br>སངས་རྒྱས་མང་པོ་བྱོན་ན་ཡང་།<br>ངེད་ལ་སུ་ཡིས་མ་བཟུང་བ།<br>ཁྱེད་ཀྱིས་བརྩེ་བས་སྐྱོང་བར་མཛད།<br>སངས་རྒྱས་སྟོང་ལས་དྲིན་ཆེ་བ།</div>
      <div class="zh" style="margin-top:20px;line-height:1.9">切莫忘记上师，<br>即使众多佛降临，<br>谁皆未曾摄受我，<br>您不舍弃悲悯护，<br>您比千佛恩更大。</div>
      <div class="en-small" style="margin-top:34px"><p>Do not forget the guru.</p><p>Although many Buddhas had appeared, none has taken hold of me.</p><p>You did not abandon me, but lovingly and compassionately protected me.</p><p>Your kindness is greater than a thousand Buddhas'.</p></div>
    </div>
    <div class="stripe"></div><div class="band"><span class="emblem" role="img" aria-label="Endless knot emblem"></span></div>
  </article>
  <article class="panel" style="left:118px">
    <div class="panel-body">
      <div class="title-zh">您与佛法</div><div class="title-en">You And The Dharma</div>
      <div class="bo-small" style="font-size:4.6px">ཆོས་སྒོ་བརྒྱད་ཁྲི་བཞི་སྟོང་གི<br>རྩ་བ་རང་སེམས་འདུལ་བ་ཡིན།<br>རང་སེམས་མ་ཐུལ་ན་གདམས་པ་འབུམ།<br>ཐོས་ཀྱང་འཆི་དུས་ཕན་མི་ཐོགས།<br>ཆོས་སྐད་ཀྱིས་མི་ཕན་ཕྱི་མར་ཡང་།<br>ཆོས་ཀྱི་སྐད་ཆ་མང་མི་དགོས།<br>རང་སེམས་ཆོས་དང་འདྲེས་ན་གྲུབ།<br>གཞན་མི་དགའ་ཡང་ཆོས་ཀྱི་རྩེ།</div>
      <div class="zh-small" style="font-size:4.8px;margin-left:46px">八万四千法门之根本，<br>乃是调伏自心一者中，<br>未伏自烦恼闻十万教，<br>临终之时亦无所助益，<br>佛法术语于来世无益，<br>对于法言无须著名声，<br>唯自心与法相融合者，<br>纵他不喜亦为法之巅，<br>由实修而得成就故，<br>是为佛法之精要。</div>
      <div class="en-small" style="margin-top:14px"><p>The eighty-four thousand Dharma doors, are solely for subduing your own mind. If your mind is not tamed despite having received countless instructions, it is hard for these instructions to help you at the time of death. When the lofty Dharma language does not benefit you at the time of death, it is harder for them to benefit you in your next life. Thus, famous teachings are not needed. Instead, your mind and the Dharma should mix internally. And when through practice, you gained certainty, that is the peak of Dharma, even if others are not delighted about it.</p></div>
    </div>
    <div class="stripe"></div><div class="band"><span class="emblem" role="img" aria-label="Conch shell emblem"></span></div>
  </article>
  <article class="panel" style="left:292px">
    <div class="panel-body">
      <div class="title-zh">要避免的错误</div><div class="title-en">Mistakes To Avoid</div>
      <div class="bo">རྐང་པ་གར་འགྲོ་ལམ་མ་ནོར།<br>སྙིང་གཏད་ས་མི་མ་ནོར།<br>སྐྱབས་བཅོལ་ས་མགོན་མ་ནོར།<br>སེམས་ཁ་བཤད་ས་གྲོགས་མ་ནོར།</div>
      <div class="zh" style="margin-top:22px;line-height:2.5">足移动处路莫误。<br>心交托处人莫误。<br>所皈依处怙莫误。<br>说心声处友莫误。</div>
      <div class="en" style="margin-top:32px;font-size:5.3px"><p>Do not tread the wrong path.<br>Do not entrust your mind to the wrong person.<br>Do not seek refuge in the wrong guardian.<br>Do not confide your thoughts to the wrong friend.</p></div>
    </div>
    <div class="stripe"></div><div class="band"><span class="emblem" role="img" aria-label="Dharma wheel emblem"></span></div>
  </article>
  <article class="panel" style="left:466px">
    <div class="panel-body">
      <div class="title-zh">别闲</div><div class="title-en">Don't Dally</div>
      <div class="bo">མ་ཡེངས་མ་ཡེངས་འཆི་བ་མྱུར།<br>འཆི་བ་གློ་བུར་བྱུང་ན་ཅི།<br>མ་ལེ་མ་ལེ་དམ་ཆོས་བརྩོན།<br>ཆོས་མེད་བར་དོར་སུ་ཡིས་སྐྱོབ།</div>
      <div class="zh" style="margin-top:18px;line-height:2.5;margin-left:26px">莫造莫造死亡迅速临。<br>死亡突然来到当何为？<br>莫停莫停精进于正法。<br>无法流转中有谁救护？</div>
      <div class="en" style="font-size:5.3px;margin-top:24px"><p>Don't be distracted, don't be distracted, for quickly death will come.</p><p>What can you do when death suddenly come?</p><p>Don't dally, don't dally, exert yourself in the excellent Dharma.</p><p>Without the Dharma, who can protect you when you wander in the bardo?</p></div>
    </div>
    <div class="stripe"></div><div class="band"><span class="emblem" role="img" aria-label="Golden fish emblem"></span></div>
  </article>
  <article class="panel" style="left:640px">
    <div class="panel-body">
      <div class="title-zh">过于污垢</div><div class="title-en">Excessive Dirt</div>
      <div class="bo">ཕྲག་དོག་ཆེ་ན་སེམས་མི་སྐྱིད།<br>རང་དོན་ཆེ་ན་གྲོགས་མི་རྙེད།<br>སྙམ་པ་ཆེ་ན་དོན་མི་འགྲུབ།<br>གཡོ་སྒྱུ་ཆེ་ན་ཡིད་མི་ཆེས།</div>
      <div class="zh" style="margin-top:22px;line-height:2.5">嫉妒若盛心不乐。<br>自利若盛友不获。<br>贪妄若盛利不成。<br>狡诈若多人不信。</div>
      <div class="en" style="font-size:5.3px;margin-top:28px"><p>If your envy is great, your mind will not be joyful.</p><p>If your self-centredness is great, you will not gain friends.</p><p>If your greed is great, your goal will not be accomplished.</p><p>If your deceitfulness is great, your credibility will be lost</p></div>
    </div>
    <div class="stripe"></div><div class="band"><span class="emblem" role="img" aria-label="Turning arrows emblem"></span></div>
  </article>
  <article class="panel" style="left:810px">
    <div class="panel-body">
      <div class="title-zh">十大遗憾（上）</div><div class="title-en">Ten Regrets (Part I)</div>
      <div class="two-col">
        <div class="bo-small">མི་ལུས་རྙེད་དཀའ་ཐོབ་ཙམ་ན།<br>མི་དགེ་ལ་དགའ་བ་འགྱོད།<br>དལ་འབྱོར་ཐོབ་ཀྱང་ཆོས་མེད་པར།<br>ཕལ་པ་ཤི་བ་འགྱོད།<br>ཚེ་ཐུང་དོན་མེད་བྱ་བ་ལ།<br>ཚེ་ཟད་པ་ནི་འགྱོད།<br>སེམས་ཉིད་ཆོས་སྐུ་མ་རྟོགས་པར།<br>འཁོར་བར་བྱིང་བ་འགྱོད།<br>བླ་མ་ལས་བྲལ་འགྱོད།</div>
        <div class="zh-small">难得人身已获得，<br>行诸恶事甚可惜；<br>已具暇满无法修，<br>凡夫死去甚可惜；<br>寿短无益之事中，<br>耗尽此生甚可惜；<br>未悟心性法身者，<br>沉溺轮回甚可惜；<br>离别上师甚可惜。</div>
      </div>
      <div class="en-small" style="margin-top:48px"><p>It is regrettable to take joy in acts of non-virtues and evil when you have this unstained human body that is hard to obtain.</p><p>It is regrettable to die as an ordinary person without the Dharma, when you have this unstained human body with leisure, wealth and properties that is hard to obtain.</p><p>It is regrettable to exhaust yourself in senseless and meaningless activities in this age of degeneration when your human lifespan is short and will pass in an instant.</p><p>It is regrettable to be sunk in the mire of samsaric confusion when your unelaborated natural mind is the nature of dharmakaya.</p><p>It is regrettable to be separated from your holy guru, the guide on the path, before you attain enlightenment.</p></div>
    </div>
    <div class="stripe"></div><div class="band"><span class="emblem" role="img" aria-label="Treasure vase emblem"></span></div>
  </article>
  <article class="panel" style="left:984px;border-right:none">
    <div class="panel-body">
      <div class="title-zh">十大遗憾（下）</div><div class="title-en">Ten Regrets (Part II)</div>
      <div class="two-col">
        <div class="bo-small">ཉམས་ལེན་མེད་པར་ཤི་བ་འགྱོད།<br>ཐོས་པ་ཆོས་སུ་མ་གྱུར་འགྱོད།<br>སྒོ་གསུམ་ཐ་མལ་བཞག་པ་འགྱོད།<br>དམ་ཚིག་ཉམས་པ་འགྱོད།<br>དགེ་བ་མ་བསགས་འགྱོད།</div>
        <div class="zh-small" style="margin:0">年少三门闲置者，<br>凡庸度日甚可惜；<br>闻法未成修持者，<br>空过此生甚可惜；<br>誓言毁坏甚可惜。</div>
      </div>
      <div class="en-small" style="margin-top:44px"><p>It is regrettable when the three doors of young adults in their prime, stay in the ordinary state of indifference (to practising the Dharma).</p><p style="font-style:italic;padding-left:8px">1. samskaras: those factors of the mind which cause (i) the aggregation into a being i.e. the taking of a rebirth; (ii) subsequent aggregation of the various forms of the five heaps of that rebirth; and (iii) the dissolution of that five heaps.</p><p style="font-style:italic;padding-left:8px">2. three doors: body, speech and mind</p></div>
      <div class="dedication">DEDICATION</div>
      <div class="bo-small" style="margin-left:8px">འགྲོ་བ་ཀུན་དང་མཉམ་དུ་སངས་རྒྱས་ཤོག</div>
      <div class="zh-small" style="margin:2px 0 0 8px">愿众有情共证佛果。</div>
      <div class="en-small" style="margin:2px 0 0 8px">May all attain Buddhahood together</div>
    </div>
    <div class="stripe"></div><div class="band"><span class="emblem" role="img" aria-label="Om syllable emblem"></span></div>
  </article>
</section>

</div>
</body>
</html>
```